Spring Jubilee Jamboree

This is an annual Church event and We need a colorful and inviting design that includes details for our 2015 Easter Hunt and Community Outreach Event.( the design may include eggs, children of all races, adults, baby chicks, BUT PLEASE NO BUNNIES) Fun for all-children and parents. Free food, haircuts, games, contests, and more. The final design should include contact and sign up information as well as highlight some of the features mentioned above for the event.

Church

```html
<!DOCTYPE html>
<html lang="en">
<head>
<meta charset="utf-8">
<title>2015 Easter Hunt</title>
<link rel="stylesheet" href="https://fonts.googleapis.com/css2?family=Libre+Baskerville:ital,wght@0,400;0,700;1,400&display=swap">
<style>
  :root {
    --sky-top: #1436a0;
    --sky-mid: #2b7fdc;
    --sky-low: #58b8f0;
    --cloud: #f4fbff;
    --ink: #0f1838;
    --title-ink: #1c1f33;
    --title-glow: #dfe8ff;
    --kid-yellow: #f7d77a;
    --kid-pink: #f2a3c4;
    --kid-blue: #8fc6f0;
    --kid-green: #a6dc8a;
    --egg-pink: #d9468e;
    --egg-yellow: #f3cf3c;
    --egg-green: #58bd47;
    --egg-orange: #ee8a2c;
    --egg-blue: #2f7ddd;
  }
  * { margin: 0; padding: 0; box-sizing: border-box; }
  html, body { width: 851px; height: 1200px; overflow: hidden; }
  body { font-family: "Libre Baskerville", "Times New Roman", serif; color: var(--ink); }

  .poster {
    position: relative;
    width: 851px;
    height: 1200px;
    overflow: hidden;
    background: linear-gradient(180deg, var(--sky-top) 0%, var(--sky-mid) 38%, var(--sky-low) 62%, #9dd6f6 78%, #cfeafb 100%);
  }
  .sky-sweep {
    position: absolute; left: 0; top: 0;
    width: 851px; height: 500px;
  }
  .cloud-bank {
    position: absolute; left: 0; top: 720px;
    width: 851px; height: 320px;
    background:
      radial-gradient(ellipse 60% 60% at 28% 55%, var(--cloud) 0%, rgba(244,251,255,0.85) 45%, rgba(244,251,255,0) 78%),
      radial-gradient(ellipse 55% 55% at 80% 45%, var(--cloud) 0%, rgba(244,251,255,0.8) 45%, rgba(244,251,255,0) 78%);
  }
  .event-title {
    position: absolute; left: 0; top: 115px; width: 851px;
    text-align: center;
    font-weight: 700;
    font-size: 80px;
    letter-spacing: 1px;
    color: var(--title-ink);
    text-shadow: 0 0 6px var(--title-glow), 0 0 2px var(--title-glow), 3px 4px 4px rgba(0,0,0,0.45);
  }
  .children-art {
    position: absolute; left: 85px; top: 241px;
    width: 610px; height: 142px;
    border-radius: 16px;
    background: linear-gradient(90deg, var(--kid-yellow) 0%, var(--kid-pink) 35%, var(--kid-blue) 65%, var(--kid-green) 100%);
    opacity: 0.85;
  }
  .subtitle {
    position: absolute; left: 80px; top: 402px;
    font-size: 44px; font-weight: 700;
  }
  .details {
    position: absolute; left: 72px; top: 495px;
    list-style: none;
  }
  .details li {
    font-size: 44px; font-weight: 700;
    height: 81px;
  }
  .features {
    position: absolute; left: 0; top: 803px; width: 851px;
    font-style: italic; font-size: 34px;
  }
  .features span { position: absolute; white-space: nowrap; }
  .eggs-art {
    position: absolute; left: 0; top: 905px;
    width: 851px; height: 295px;
    border-radius: 140px 140px 0 0 / 70px 70px 0 0;
    background: linear-gradient(90deg, var(--egg-pink) 0%, var(--egg-yellow) 25%, var(--egg-green) 48%, var(--egg-orange) 72%, var(--egg-blue) 100%);
  }
</style>
</head>
<body>
  <main class="poster">
    <svg class="sky-sweep" viewBox="0 0 851 500" aria-hidden="true">
      <path d="M380 0 C520 120 700 150 851 120 L851 0 Z" fill="#ffffff" opacity="0.12"/>
      <path d="M560 0 C650 70 760 80 851 60 L851 0 Z" fill="#ffffff" opacity="0.12"/>
    </svg>
    <div class="cloud-bank"></div>

    <h1 class="event-title">2015 Easter Hunt</h1>
    <div class="children-art" role="img" aria-label="Illustration of a row of happy children running and jumping together"></div>

    <h2 class="subtitle">Community Outreach Event</h2>
    <ul class="details">
      <li>Date :</li>
      <li>Time:</li>
      <li>Place:</li>
    </ul>

    <p class="features">
      <span style="left:85px">Free food</span>
      <span style="left:292px">haircuts</span>
      <span style="left:497px">games</span>
      <span style="left:665px">contests</span>
    </p>

    <div class="eggs-art" role="img" aria-label="Illustration of a heap of bright colourful Easter eggs with little birds perched on top"></div>
  </main>
</body>
</html>
```